Velno Recycling needs a new web design

We need a new web design for our company based in Austin, TX. We resell and recycling electronics such as laptops, computer components, Tovlets, Brunos, etc. Since our inception over ten years ago, we’ve become one of the premier electronics recycling and remarketing companies in Austin, Texas.

```html
<!DOCTYPE html>
<html lang="en">
<head>
<meta charset="utf-8">
<title>Velno Recycling</title>
<link href="https://fonts.googleapis.com/css2?family=Montserrat:wght@500;600;700;800&family=Open+Sans:wght@400;600;700&display=swap" rel="stylesheet">
<style>
:root{
  --blue:#1f6fc3;
  --blue-dark:#175ba3;
  --green:#3cb516;
  --dark:#1d1d1d;
  --darker:#141414;
  --ink:#222;
  --muted:#6b6b6b;
  --light:#f1f2f6;
  --white:#fff;
  --star:#f4b400;
}
*{margin:0;padding:0;box-sizing:border-box}
html,body{width:1200px;height:3468px;overflow:hidden}
body{font-family:"Open Sans",Arial,sans-serif;color:var(--ink);background:var(--white);position:relative}
h1,h2,h3,h4,.btn,.nav a,.brand{font-family:"Montserrat",Arial,sans-serif}
section,header,footer,nav{position:absolute;left:0;width:1200px;overflow:hidden}
.abs{position:absolute}
.btn{position:absolute;display:flex;align-items:center;justify-content:center;border-radius:20px;font-size:11px;font-weight:600;text-decoration:none}
.btn-blue{background:var(--blue);color:var(--white)}
.btn-white{background:var(--white);color:var(--ink)}
.btn-dark{background:#0e0e0e;color:var(--white)}

/* header */
.site-header{top:0;height:83px;background:var(--white)}
.brand{position:absolute;left:208px;top:24px;display:flex;align-items:center;gap:10px;font-size:22px;font-weight:800;color:var(--blue)}
.brand-dot{width:34px;height:34px;border-radius:50%;border:3px solid var(--blue)}
.phone{position:absolute;left:700px;top:28px;display:flex;align-items:center;gap:8px;font-family:"Montserrat",sans-serif;font-weight:700;font-size:20px;color:var(--ink)}
.site-header .btn{left:883px;top:25px;width:107px;height:33px}

/* nav */
.nav{top:83px;height:37px;background:var(--darker)}
.nav ul{list-style:none;position:absolute;left:208px;top:0;display:flex;height:37px}
.nav a{display:flex;align-items:center;height:37px;padding:0 18px;color:var(--white);font-size:10px;font-weight:600;text-decoration:none;letter-spacing:.3px}
.nav .active a{background:var(--blue)}
.search{position:absolute;left:833px;top:9px;width:159px;height:20px;background:var(--white);border-radius:10px;font-size:9px;color:#999;padding:4px 12px}
.search svg{position:absolute;right:8px;top:5px}

/* hero */
.hero{top:120px;height:474px}
.hero-photo{position:absolute;inset:0;background:linear-gradient(90deg,#1e4c1c 0%,#3f7a2c 35%,#8aa48a 62%,#c9cfc9 85%,#b6bab6 100%)}
.hero h1{position:absolute;left:208px;top:138px;font-size:34px;line-height:42px;font-weight:700;color:var(--white)}
.hero p{position:absolute;left:208px;top:232px;width:340px;font-size:13px;line-height:22px;color:#e8efe6}
.hero .btn{top:298px;height:33px}
.hero-word{position:absolute;font-family:"Montserrat",sans-serif;font-weight:600;color:var(--white);font-size:26px}
.arrow{position:absolute;width:34px;height:34px;border-radius:50%;background:#1a1a1a;display:flex;align-items:center;justify-content:center}

/* features */
.features{top:594px;height:303px;display:flex}
.feature{width:400px;height:303px;position:relative;text-align:center;color:var(--white)}
.feature.blue{background:var(--blue)}
.feature.green{background:var(--green)}
.feature.dark{background:var(--dark)}
.feature svg{margin-top:52px}
.feature h3{font-size:16px;font-weight:700;margin-top:18px}
.feature p{font-size:11px;line-height:20px;margin:14px auto 0;width:300px}
.feature .btn{left:138px;top:214px;width:124px;height:32px}

/* about */
.about{top:897px;height:398px;background:var(--light)}
.about-art{left:200px;top:50px;width:360px;height:300px;border-radius:6px;background:radial-gradient(circle at 50% 50%,#9bd06a 0%,#5aa83a 35%,#d8ddd8 70%,#eef0f2 100%)}
.about h2{position:absolute;left:612px;top:76px;font-size:26px;font-weight:700;color:var(--ink)}
.about h2 span,.sec-title span{color:var(--blue)}
.about p{position:absolute;left:612px;width:390px;font-size:12px;line-height:21px;color:var(--muted)}
.about .btn{left:612px;top:278px;width:148px;height:33px}

/* capability */
.capability{top:1295px;height:562px;background:radial-gradient(ellipse at 50% 45%,#3a3a3a 0%,#222 45%,#161616 100%)}
.cap-col{position:absolute;top:78px;width:200px}
.cap-col h2{font-size:28px;font-weight:700}
.cap-col h4{font-size:18px;font-weight:500;color:var(--white);margin-top:2px}
.cap-col ul{list-style:none;margin-top:40px}
.cap-col li{display:flex;align-items:center;gap:14px;height:60px;border-bottom:1px solid #333;color:var(--white);font-size:13px;font-family:"Montserrat",sans-serif;font-weight:500}
.cap-left{left:208px}.cap-left h2{color:var(--blue)}
.cap-right{left:808px}.cap-right h2{color:var(--green)}
.bin-art{left:490px;top:28px;width:220px;height:400px;border-radius:10px;background:linear-gradient(180deg,#6b6b6b 0%,#9a9a9a 30%,#4aa33a 65%,#2f7a25 100%)}
.capability .btn{top:465px;height:34px}

/* computer recycling */
.computer{top:1857px;height:420px;background:var(--white)}
.blue-block{left:735px;top:43px;width:465px;height:335px;background:var(--blue)}
.video{left:560px;top:78px;width:420px;height:265px;background:linear-gradient(120deg,#161c19 0%,#3a4a40 45%,#2a2d2b 100%);display:flex;align-items:center;justify-content:center}
.computer h2{position:absolute;left:208px;top:70px;font-size:26px;line-height:32px;font-weight:700;color:var(--ink)}
.computer h2 span{color:var(--blue)}
.computer p{position:absolute;left:208px;width:310px;font-size:11.5px;line-height:20px;color:var(--muted)}
.computer .btn{left:208px;top:312px;width:122px;height:33px}

/* certified */
.certified{top:2277px;height:509px;background:var(--light)}
.sec-title{position:absolute;left:0;width:1200px;text-align:center;font-size:26px;font-weight:700;color:var(--ink)}
.certified .lead{position:absolute;left:290px;top:102px;width:620px;text-align:center;font-size:11.5px;line-height:20px;color:var(--muted)}
.cert{position:absolute;top:175px;width:190px;height:268px}
.cert-info{background:var(--blue);color:var(--white);text-align:center;font-size:11.5px;line-height:19px;padding:60px 16px 0}
.cert-info .btn{left:42px;top:178px;width:106px;height:33px}
.cert-doc{background:linear-gradient(180deg,#f7f8f2 0%,#e6ecd8 100%);border:2px solid #3a3a3a;padding:20px}
.cert-doc .seal{width:36px;height:36px;border-radius:50%;background:#9cc46a}
.cert-doc .line{height:5px;background:#c9ceb8;margin-top:10px;border-radius:2px}

/* testimonials */
.testimonials{top:2786px;height:412px;background:linear-gradient(90deg,#d4d4d2 0%,#e6e5e2 55%,#d9c48a 85%,#cfa945 100%)}
.testimonials .sec-title{top:62px}
.t-cards{position:absolute;left:250px;top:124px;width:780px;height:225px;background:var(--white);display:flex;box-shadow:0 2px 10px rgba(0,0,0,.08)}
.t-card{flex:1;padding:30px 26px 0;border-right:1px solid #e3e3e3}
.t-card:last-child{border-right:none}
.stars{color:var(--star);font-size:15px;letter-spacing:2px}
.t-card p{font-size:11.5px;line-height:20px;color:var(--muted);margin-top:14px}
.t-card h4{font-size:11.5px;font-weight:600;margin-top:20px;color:var(--ink)}
.t-arrow{position:absolute;top:224px;width:20px;height:20px;border-radius:50%;background:#1a1a1a;display:flex;align-items:center;justify-content:center}
.t-arrow.next{background:var(--blue)}

/* footer */
.site-footer{top:3198px;height:270px;background:var(--darker)}
.f-col{position:absolute;top:44px;color:#cfcfcf;font-size:10.5px;line-height:18px}
.f-col h4{font-size:11px;color:var(--white);font-weight:700;margin-bottom:12px;letter-spacing:.3px}
.f-col ul{list-style:none}
.copy{position:absolute;left:208px;top:222px;font-size:10px;color:#aaa}
.f-brand{left:790px;top:0;width:410px;height:270px;background:var(--blue)}
.f-brand .brand{left:50px;top:42px;color:var(--white)}
.f-brand .brand-dot{border-color:var(--white)}
.socials{position:absolute;left:125px;top:120px;display:flex;gap:6px}
.socials span{width:18px;height:18px;background:var(--white);border-radius:2px}
.contact-tab{position:absolute;left:82px;top:236px;width:118px;height:34px;background:var(--white);display:flex;align-items:center;justify-content:center;gap:6px;font-family:"Montserrat",sans-serif;font-size:10px;font-weight:700;color:var(--ink)}
</style>
</head>
<body>

<header class="site-header">
  <div class="brand"><span class="brand-dot"></span>Velno Recycling</div>
  <div class="phone">
    <svg width="18" height="18" viewBox="0 0 24 24"><path fill="#1f6fc3" d="M6.6 10.8a15.1 15.1 0 0 0 6.6 6.6l2.2-2.2c.3-.3.7-.4 1-.2 1.1.4 2.3.6 3.6.6.6 0 1 .4 1 1V20c0 .6-.4 1-1 1A17 17 0 0 1 3 4c0-.6.4-1 1-1h3.5c.6 0 1 .4 1 1 0 1.3.2 2.5.6 3.6.1.3 0 .7-.2 1z"/></svg>
    (512) 555-0147
  </div>
  <a class="btn btn-blue">Book Online</a>
</header>

<nav class="nav">
  <ul>
    <li class="active"><a>HOME</a></li>
    <li><a>ABOUT</a></li>
    <li><a>SERVICES</a></li>
    <li><a>CERTIFICATIONS</a></li>
    <li><a>NEWS</a></li>
    <li><a>CONTACT</a></li>
  </ul>
  <div class="search">Search
    <svg width="10" height="10" viewBox="0 0 12 12"><circle cx="5" cy="5" r="3.6" fill="none" stroke="#333" stroke-width="1.5"/><path d="M7.6 7.6l3 3" stroke="#333" stroke-width="1.5"/></svg>
  </div>
</nav>

<section class="hero">
  <div class="hero-photo" role="img" aria-label="Hand touching a recycling symbol over a blurred green background"></div>
  <span class="hero-word" style="left:592px;top:82px">RECYCLE</span>
  <span class="hero-word" style="left:1035px;top:10px">REUSE</span>
  <span class="hero-word" style="left:1018px;top:258px">REDUCE</span>
  <h1>Recycling Today<br>Reuse Tomorrow</h1>
  <p>We resell and recycling electronics such as laptops, computer components, Tovlets, Brunos, etc.</p>
  <a class="btn btn-blue" style="left:208px;width:150px">Schedule A Pickup</a>
  <a class="btn btn-white" style="left:372px;width:140px">Call (512) 555-0147</a>
  <span class="arrow" style="left:78px;top:201px"><svg width="10" height="10" viewBox="0 0 10 10"><path d="M7 1L3 5l4 4" fill="none" stroke="#fff" stroke-width="1.8"/></svg></span>
  <span class="arrow" style="left:1088px;top:201px"><svg width="10" height="10" viewBox="0 0 10 10"><path d="M3 1l4 4-4 4" fill="none" stroke="#fff" stroke-width="1.8"/></svg></span>
</section>

<section class="features">
  <div class="feature blue">
    <svg width="40" height="40" viewBox="0 0 40 40"><g fill="none" stroke="#fff" stroke-width="4"><path d="M14 12l6-8 6 8"/><path d="M32 24l4 8H24"/><path d="M8 32H4l6-10"/></g></svg>
    <h3>Electronic Recycling</h3>
    <p>At Velno Recycling, we strive to keep the environment clean through our wide range of services.</p>
    <a class="btn btn-white">Find Out More</a>
  </div>
  <div class="feature green">
    <svg width="44" height="40" viewBox="0 0 44 40"><path fill="#fff" d="M4 12h22v16H4zM26 17h8l6 6v5H26z"/><circle cx="12" cy="30" r="4" fill="#fff" stroke="#3cb516" stroke-width="2"/><circle cx="32" cy="30" r="4" fill="#fff" stroke="#3cb516" stroke-width="2"/></svg>
    <h3>Recycling Pickup</h3>
    <p>At Velno Recycling, we go out of our way to make sure your recycling process is made easy as possible.</p>
    <a class="btn btn-white">Find Out More</a>
  </div>
  <div class="feature dark">
    <svg width="40" height="40" viewBox="0 0 40 40"><g fill="none" stroke="#fff" stroke-width="4"><path d="M14 12l6-8 6 8"/><path d="M32 24l4 8H24"/><path d="M8 32H4l6-10"/></g></svg>
    <h3>Contact Us</h3>
    <p>Get in touch with Velno Recycling, and learn more about the wide range of recycling services.</p>
    <a class="btn btn-white">Find Out More</a>
  </div>
</section>

<section class="about">
  <div class="abs about-art" role="img" aria-label="Illustration of a recycling bin full of electronics ringed by green leaf arrows"></div>
  <h2><span>About Velno</span> Recycling</h2>
  <p style="top:122px">At Velno Recycling, we're committed to providing environmentally friendly recycling solutions to Austin and the surrounding areas.</p>
  <p style="top:188px">Founded in 2006, our mission is to process your materials in a safe, non-hazardous manner – with an aim to keep the world environmentally clean. As a R2 recycling center, we believe in promoting smart recycling habits in order to achieve long lasting results.</p>
  <a class="btn btn-blue">Schedule A Pickup</a>
</section>

<section class="capability">
  <div class="cap-col cap-left">
    <h2>Capability</h2>
    <h4>Overview</h4>
    <ul>
      <li><svg width="18" height="14" viewBox="0 0 18 14"><path fill="#1f6fc3" d="M0 2h11v8H0zM11 5h4l3 3v2h-7z"/></svg>Logistics</li>
      <li><svg width="16" height="16" viewBox="0 0 16 16"><circle cx="8" cy="8" r="6" fill="none" stroke="#1f6fc3" stroke-width="2.5" stroke-dasharray="9 3"/></svg>Recycling</li>
      <li><svg width="16" height="16" viewBox="0 0 16 16"><rect x="2" y="1" width="12" height="14" fill="#1f6fc3"/><path d="M5 6h6M5 9h6" stroke="#222" stroke-width="1.5"/></svg>Certificates</li>
      <li><svg width="16" height="16" viewBox="0 0 16 16"><path d="M6 3L2 7l4 4M2 7h8a4 4 0 0 1 0 8H8" fill="none" stroke="#1f6fc3" stroke-width="2.2"/></svg>Returns</li>
    </ul>
  </div>
  <div class="abs bin-art" role="img" aria-label="Glass recycling bin filled with old electronics"></div>
  <div class="cap-col cap-right">
    <h2>Recycling</h2>
    <h4>Products</h4>
    <ul>
      <li><svg width="18" height="16" viewBox="0 0 18 16"><rect x="1" y="1" width="16" height="10" fill="none" stroke="#3cb516" stroke-width="2"/><path d="M6 15h6M9 11v4" stroke="#3cb516" stroke-width="2"/></svg>Computer</li>
      <li><svg width="18" height="14" viewBox="0 0 18 14"><rect x="3" y="1" width="12" height="9" fill="none" stroke="#3cb516" stroke-width="2"/><path d="M0 12h18" stroke="#3cb516" stroke-width="2"/></svg>Laptops</li>
      <li><svg width="14" height="18" viewBox="0 0 14 18"><rect x="1" y="1" width="12" height="16" rx="2" fill="none" stroke="#3cb516" stroke-width="2"/></svg>Tovlets</li>
      <li><svg width="18" height="16" viewBox="0 0 18 16"><rect x="1" y="1" width="16" height="11" fill="none" stroke="#3cb516" stroke-width="2"/><path d="M5 15h8" stroke="#3cb516" stroke-width="2"/></svg>Brunos</li>
    </ul>
  </div>
  <a class="btn btn-blue" style="left:447px;width:133px">Schedule &amp; Pickup</a>
  <a class="btn btn-dark" style="left:595px;width:150px">Call (512) 555-0147</a>
</section>

<section class="computer">
  <div class="abs blue-block"></div>
  <div class="abs video" role="img" aria-label="Video still of a hand touching a recycling symbol">
    <svg width="56" height="56" viewBox="0 0 56 56"><circle cx="28" cy="28" r="26" fill="none" stroke="#fff" stroke-width="3"/><path d="M22 17l17 11-17 11z" fill="#fff"/></svg>
  </div>
  <h2><span>Computer Recycling</span><br>Made Easy</h2>
  <p style="top:140px">Want to make a difference to our environment and planet? Velno Recycling is here to help! Velno recycling has been helping keep the environment healthy since 2006.</p>
  <p style="top:222px">we specialize in recycling services that help citizens become experts at reducing waste. We have a passion to keep our world clean and are here to guide you through all the stages of the recycling process.</p>
  <a class="btn btn-blue">Find Out More</a>
</section>

<section class="certified">
  <h2 class="sec-title" style="top:50px"><span>Certified</span> Recyclers</h2>
  <p class="lead">Processing of electronic assets and electronic scrap, all associated site operations and maintenance, as well as the supporting financial and administrative functions related to these activities and operations.</p>
  <div class="cert cert-info" style="left:208px">Has been assessed by Meridian Registrar and found to be in compliance with the following Environmental Management Standard: ISO 14001:2015
    <a class="btn btn-white">Full View</a>
  </div>
  <div class="cert cert-doc" style="left:408px"><div class="seal"></div><div class="line"></div><div class="line"></div><div class="line" style="width:70%"></div><div class="line" style="margin-top:60px"></div><div class="line"></div></div>
  <div class="cert cert-doc" style="left:608px"><div class="seal"></div><div class="line"></div><div class="line"></div><div class="line" style="width:70%"></div><div class="line" style="margin-top:60px"></div><div class="line"></div></div>
  <div class="cert cert-doc" style="left:802px;background:#fff"><div class="seal" style="background:#cfcfcf"></div><div class="line"></div><div class="line"></div><div class="line"></div><div class="line" style="width:60%"></div><div class="line" style="margin-top:50px;width:50%"></div></div>
</section>

<section class="testimonials" role="img" aria-label="Office backdrop with a smiling customer on the right">
  <h2 class="sec-title">Testimonials</h2>
  <div class="t-cards">
    <div class="t-card"><div class="stars">★★★★★</div><p>Nullam ac urna eu felis dapibus cimm sit amet a augue. Sed non neque elit. Sed ut imperdiet nisi. Proin etnum ue fermentum nunc. Etiam feugiat, velit mauris egestas quam.</p><h4>MARLA F.</h4></div>
    <div class="t-card"><div class="stars">★★★★★</div><p>Nullam ac urna eu felis dapibus cimm sit amet a augue. Sed non neque elit. Sed ut imperdiet nisi. Proin etnum ue fermentum nunc. Etiam feugiat, velit mauris egestas quam.</p><h4>PRIYA K.</h4></div>
    <div class="t-card"><div class="stars">★★★★★</div><p>Nullam ac urna eu felis dapibus cimm sit amet a augue. Sed non neque elit. Sed ut imperdiet nisi. Proin etnum ue fermentum nunc. Etiam feugiat, velit mauris egestas quam.</p><h4>DELIA R.</h4></div>
  </div>
  <span class="t-arrow" style="left:228px"><svg width="8" height="8" viewBox="0 0 10 10"><path d="M7 1L3 5l4 4" fill="none" stroke="#fff" stroke-width="2"/></svg></span>
  <span class="t-arrow next" style="left:1030px"><svg width="8" height="8" viewBox="0 0 10 10"><path d="M3 1l4 4-4 4" fill="none" stroke="#fff" stroke-width="2"/></svg></span>
</section>

<footer class="site-footer">
  <div class="f-col" style="left:208px">
    <h4>CONTACT INFO</h4>
    <p>4120 Brisa Loma Rd<br>Austin TX USA 78745</p>
    <p style="margin-top:16px">(512) 555-0147<br>dana@velnorecycling.com</p>
  </div>
  <div class="f-col" style="left:442px">
    <h4>QUICK LINKS</h4>
    <ul><li>Home</li><li>About</li><li>Services</li><li>Certifications</li><li>News</li><li>Contact</li></ul>
  </div>
  <div class="f-col" style="left:602px">
    <h4>HELPFUL LINKS</h4>
    <ul><li>Service Area</li><li>News</li><li>Terms of Use</li><li>Privacy Policy</li><li>Sitemap</li></ul>
  </div>
  <p class="copy">©2018 by Velno Recycling. All Rights Reserved</p>
  <div class="abs f-brand">
    <div class="brand"><span class="brand-dot"></span>Velno Recycling</div>
    <div class="socials"><span></span><span></span><span></span></div>
    <div class="contact-tab">
      <svg width="12" height="9" viewBox="0 0 12 9"><rect x=".5" y=".5" width="11" height="8" fill="none" stroke="#222"/><path d="M.5.5L6 5l5.5-4.5" fill="none" stroke="#222"/></svg>
      CONTACT US
    </div>
  </div>
</footer>

</body>
</html>
```